RT Consult - Web Design Upgrade

We have recently designed a website (http://www.rtconsult-demo.com.au) which requires more creative and professional inputs. The website was designed using 'jolly portals site builder template' and it is currently available for viewing on the internet. Also, you are able to access the PDF files for the 6 main pages (i.e. Home, About, Services, Contaminated Land Management, Groundwater Management and Contact).

The current website has 17 pages, however, your design may only be required for the 6 main pages.

Currently the website background is white but we are open to other colours provided the company logo is adjusted accordingly.

The idea is to upgrade the existing design and, if possible, continue using 'jolly portals' as the preferred web host. So we are not sure if the design should be coded or uncoded...we leave it to your proficiency and advice.

Target Market(s)

Government organisations, landowners and developers, waste and utilities companies, community organisations and individuals.

Industry/Entity Type

Internet

Number of Pages Required

5+ page

Font styles to use
Sans Serif

Colors
0355a3
3176b5
9ccb3b
acd037
ffffff

Requirements
Nice to have
• Sliding images

```html
<!DOCTYPE html>
<html lang="en">
<head>
<meta charset="utf-8">
<title>RT Consult — Home</title>
<link href="https://fonts.googleapis.com/css2?family=Open+Sans:wght@400;600;700&family=Arimo:wght@400&display=swap" rel="stylesheet">
<style>
:root{
  --blue:#0355a3;
  --blue-soft:#3176b5;
  --green:#9ccb3b;
  --green-alt:#acd037;
  --green-dark:#7aa82a;
  --white:#ffffff;
  --text-grey:#8a8a8a;
  --text-dark:#444444;
  --line:#e6e6e6;
  --footer:#3d3d3d;
  --footer-line:#5a5a5a;
}
*{box-sizing:border-box;margin:0;padding:0}
html,body{width:897px;height:1200px;overflow:hidden;background:var(--white)}
body{position:relative;font-family:"Arimo",Arial,sans-serif;color:var(--text-grey)}
.abs{position:absolute}

/* header */
.top-rule{left:0;top:0;width:897px;height:2px;background:var(--green)}
.brand{left:98px;top:14px;display:flex;align-items:center;gap:8px}
.brand-mark{width:22px;height:22px;border-radius:50%;background:var(--green)}
.brand-name{font-family:"Open Sans",sans-serif;font-weight:700;font-size:22px;color:var(--blue)}
.search{left:601px;top:39px;width:198px;height:28px;border:1px solid #cfcfcf;display:flex;align-items:center;justify-content:space-between;padding:0 10px 0 11px;font-family:"Open Sans",sans-serif;font-size:7.5px;color:#999}

/* nav */
.nav{left:0;top:104px;width:897px;height:44px;background:linear-gradient(#a6d043,#8fc031);border-bottom:3px solid #c6e08a}
.nav ul{list-style:none;position:absolute;left:98px;top:0;display:flex;height:41px}
.nav li{font-family:"Open Sans",sans-serif;font-size:9.8px;color:var(--white);line-height:41px;padding:0 19px;text-transform:uppercase}
.nav li.active{background:var(--green-dark)}

/* hero */
.hero{left:0;top:148px;width:897px;height:398px;background:linear-gradient(#3f4652 0%,#7d838c 30%,#5d6c55 50%,#8da0b0 70%,#6f8060 100%)}
.hero-title{left:0;top:222px;width:897px;text-align:center;font-family:"Open Sans",sans-serif;font-weight:600;font-size:55px;color:var(--green);letter-spacing:-.5px}
.hero-sub{left:0;top:293px;width:897px;text-align:center;font-family:"Open Sans",sans-serif;font-size:18.5px;color:var(--white)}
.arrow{top:318px}
.thumbs{left:206px;top:450px;width:487px;height:83px;background:rgba(255,255,255,.35);display:flex;gap:16px;padding:13px 0 0 14px}
.thumb{width:103px;height:57px;border:3px solid var(--white)}

/* welcome */
.welcome-title{left:0;top:567px;width:897px;text-align:center;font-family:"Open Sans",sans-serif;font-weight:600;font-size:21px;color:var(--blue)}
.accent{color:var(--green)}
.welcome-text{left:140px;top:608px;width:617px;text-align:center;font-size:8.6px;line-height:19.5px}
.divider{left:98px;top:685px;width:701px;height:1px;background:var(--line)}

/* services & news */
.section-title{top:702px;font-family:"Open Sans",sans-serif;font-weight:600;font-size:21px;color:var(--blue)}
.service{top:745px;width:222px}
.service-photo{width:222px;height:125px}
.service-name{margin-top:12px;font-size:10px;color:var(--blue-soft);text-transform:uppercase}
.service-text{margin-top:5px;font-size:8.3px;line-height:16.8px}
.news{left:576px;width:223px;height:89px;background:#f7f7f7;border:1px solid #ececec;border-left:4px solid var(--blue-soft);padding:9px 0 0 14px}
.news-date{font-size:9.6px;color:var(--text-dark)}
.news-text{margin-top:5px;font-size:8.3px;line-height:16px;color:#9a9a9a}

/* footer */
.footer{left:0;top:983px;width:897px;height:217px;background:var(--footer)}
.footer-bottom-rule{left:0;top:1196px;width:897px;height:4px;background:var(--green)}
.f-head{font-size:12.5px;color:var(--white);text-transform:uppercase}
.f-text{font-size:8.4px;line-height:16.9px;color:var(--white);margin-top:8px}
.socials{display:flex;gap:6px;margin-top:8px}
.social{width:23px;height:23px;border:1px solid var(--white);background:#2e2e2e}
.email-field{margin-top:7px;width:159px;height:22px;border:1px solid var(--white);font-size:7.5px;color:var(--white);line-height:20px;padding-left:8px}
.subscribe{margin-top:8px;width:61px;height:21px;border:1px solid var(--white);font-size:7.5px;color:var(--white);line-height:19px;text-align:center}
.f-divider{left:98px;top:1152px;width:704px;height:1px;background:var(--footer-line)}
.copyright{left:0;top:1171px;width:897px;text-align:center;font-size:8.4px;color:var(--white)}
</style>
</head>
<body>
<div class="abs top-rule"></div>

<header>
  <div class="abs brand"><span class="brand-mark"></span><span class="brand-name">RT Consult</span></div>
  <div class="abs search"><span>SEARCH</span>
    <svg width="9" height="9" viewBox="0 0 9 9"><circle cx="3.6" cy="3.6" r="2.7" fill="none" stroke="#999" stroke-width="1.3"/><line x1="5.6" y1="5.6" x2="8.4" y2="8.4" stroke="#999" stroke-width="1.5"/></svg>
  </div>
</header>

<nav class="abs nav">
  <ul>
    <li class="active">Home</li><li>About</li><li>Services</li><li>Contaminated Land Management</li><li>Groundwater Management</li><li>Contact</li>
  </ul>
</nav>

<section class="abs hero" role="img" aria-label="Wetland landscape at sunset under a cloudy sky"></section>
<div class="abs hero-title">STRATEGICADVICE</div>
<div class="abs hero-sub">WORKING TO SUSTAIN OUR ENVIRONMENTS</div>
<svg class="abs arrow" style="left:54px" width="30" height="60" viewBox="0 0 30 60"><polyline points="29,1 1,30 29,59" fill="none" stroke="#fff" stroke-width="1.2"/></svg>
<svg class="abs arrow" style="left:819px" width="30" height="60" viewBox="0 0 30 60"><polyline points="1,1 29,30 1,59" fill="none" stroke="#fff" stroke-width="1.2"/></svg>
<div class="abs thumbs">
  <div class="thumb" role="img" aria-label="Wetland at sunset" style="background:linear-gradient(#3d4550,#7b8c6a)"></div>
  <div class="thumb" role="img" aria-label="Two consultants reviewing plans in a field" style="background:linear-gradient(#2b4fb0,#5f7a3a)"></div>
  <div class="thumb" role="img" aria-label="Aerial view of an industrial site" style="background:linear-gradient(#6d7a6a,#9a9890)"></div>
  <div class="thumb" role="img" aria-label="Drilling rig at a work site" style="background:linear-gradient(#6e7c8a,#a89a50)"></div>
</div>

<h1 class="abs welcome-title">WELCOME TO <span class="accent">RT CONSULT</span></h1>
<p class="abs welcome-text">Sed ut perspiciatis unde omnis iste natus error sit voluptatem accusantium doloremque laudantium, totam rem aperiam, eaque ipsa quae ab illo inventore veritatis et quasi architecto beatae vitae dicta sunt explicabo. Nemo enim ipsam voluptatem quia voluptas sit aspernatur aut odit aut fugit, sed quia consequuntur magni dolores eos qui ratione voluptatem sequi nesciunt.</p>
<div class="abs divider"></div>

<h2 class="abs section-title" style="left:98px">OUR <span class="accent">SERVICES</span></h2>
<article class="abs service" style="left:98px">
  <div class="service-photo" role="img" aria-label="Two consultants kneeling in a field studying a site plan" style="background:linear-gradient(#1f3fb8 0%,#4a6ad0 55%,#6f7d3a 100%)"></div>
  <h3 class="service-name">Contaminated Land Management</h3>
  <p class="service-text">Sed ut perspiciatis unde omnis iste natus error sit voluptatem accusantium doloremque laudantium, totam rem architecto beatae vitae dicta sunt explicabo.</p>
</article>
<article class="abs service" style="left:334px">
  <div class="service-photo" role="img" aria-label="Field workers in safety vests sampling a groundwater well" style="background:linear-gradient(#8d9096 0%,#9a8a80 50%,#7a5a48 100%)"></div>
  <h3 class="service-name">Groundwater Management</h3>
  <p class="service-text">Sed ut perspiciatis unde omnis iste natus error sit voluptatem accusantium doloremque laudantium, totam rem architecto beatae vitae dicta sunt explicabo.</p>
</article>

<h2 class="abs section-title" style="left:576px">LATEST <span class="accent">NEWS</span></h2>
<article class="abs news" style="top:745px">
  <div class="news-date">December 10,2014</div>
  <p class="news-text">Sed ut perspiciatis unde omnis iste natus error sit voluptatem accusantium doloremque laudantium, ab illo invensunt explicabo.</p>
</article>
<article class="abs news" style="top:848px">
  <div class="news-date">December 10,2014</div>
  <p class="news-text">Sed ut perspiciatis unde omnis iste natus error sit voluptatem accusantium doloremque laudantium, ab illo invensunt explicabo.</p>
</article>

<footer class="abs footer"></footer>
<div class="abs" style="left:106px;top:1002px;width:190px">
  <h4 class="f-head">About Us</h4>
  <p class="f-text">Sed ut perspiciatis unde omnis iste natus error sit voluptatem accusantium doloremque laudantium, totam rem aperiam, eaque ipsa quae ab illo inventore veritatis et quasi architecto beatae vitae dicta sunt explicabo.......</p>
</div>
<div class="abs" style="left:323px;top:1002px;width:160px">
  <h4 class="f-head">Contact Us</h4>
  <p class="f-text">Address : 48 Kestrel Lane,<br>Marrowdale, NSW 2999</p>
  <p class="f-text" style="margin-top:3px">Phone : 61 (0)400 000 123</p>
  <p class="f-text" style="margin-top:4px">Email :info@rtconsult-demo.com</p>
</div>
<div class="abs" style="left:492px;top:1002px;width:120px">
  <h4 class="f-head">Recent Posts</h4>
  <p class="f-text">Strategic Advice<br>Project Management<br>Purchase/Sale<br>Contamination<br>Apraisal</p>
</div>
<div class="abs" style="left:631px;top:1002px;width:170px">
  <h4 class="f-head">Connect With Us</h4>
  <div class="socials">
    <span class="social" aria-label="Social link"></span><span class="social" aria-label="Social link"></span><span class="social" aria-label="Social link"></span><span class="social" aria-label="Social link"></span>
  </div>
  <h4 class="f-head" style="margin-top:16px">Get Newsletter</h4>
  <div class="email-field">EMAIL ADDRESS :</div>
  <div class="subscribe">SUBSCRIBE</div>
</div>
<div class="abs f-divider"></div>
<div class="abs copyright">© Copy Rights 2014 RT Consult.All Rights Reserved.</div>
<div class="abs footer-bottom-rule"></div>
</body>
</html>
```